business card design for luxurious real estate brand

using the attached logo, i am looking for a 2-sided business card design. the back should be the gold logo on black background. the front needs to include: gold logo, name, phone, email, and website

Industry/Entity Type

real estate

Contact Information for Business Card

logo, name, email, phone, website

Font styles to use
Sans Serif

```html
<!DOCTYPE html>
<html lang="en">
<head>
<meta charset="utf-8">
<title>Casa Verlaine — Business Card</title>
<link href="https://fonts.googleapis.com/css2?family=Poppins:wght@400;500;600&display=swap" rel="stylesheet">
<style>
  :root {
    --page-bg: #0c0c0d;
    --card-bg: #27272a;
    --card-back-bg: #242426;
    --gold: #ffcb05;
    --text-light: #d9d9db;
    --rule: #4a4a4e;
    --emboss: #3d3d41;
  }
  * { margin: 0; padding: 0; box-sizing: border-box; }
  html, body {
    width: 1200px; height: 820px; overflow: hidden;
    background: var(--page-bg);
    font-family: "Poppins", sans-serif;
  }
  .stage {
    position: relative; width: 1200px; height: 820px;
    display: flex; align-items: center; justify-content: center; gap: 50px;
  }
  .card {
    position: relative; width: 520px; height: 300px;
    background: var(--card-bg);
    border-bottom: 3px solid var(--gold);
    border-left: 3px solid var(--gold);
    box-shadow: 0 20px 40px rgba(0,0,0,.6);
  }
  .card--back { background: var(--card-back-bg); display: flex; align-items: center; justify-content: center; }

  .brand { display: flex; align-items: center; gap: 12px; }
  .brand__mark { width: 14px; height: 14px; }
  .brand__name { font-weight: 500; letter-spacing: 6px; text-transform: uppercase; white-space: nowrap; }

  .card--front .brand { position: absolute; top: 62px; right: 36px; }
  .card--front .brand__mark { background: var(--gold); }
  .card--front .brand__name { color: var(--gold); font-size: 24px; }

  .card--back .brand__mark { background: var(--emboss); width: 16px; height: 16px; }
  .card--back .brand__name { color: var(--emboss); font-size: 28px; letter-spacing: 7px; }

  .person { position: absolute; left: 30px; top: 132px; }
  .person__name { color: var(--gold); font-weight: 600; font-size: 19px; line-height: 24px; text-transform: uppercase; }
  .person__title { color: var(--text-light); font-size: 13px; line-height: 18px; }

  .divider { position: absolute; left: 30px; right: 30px; top: 184px; height: 1px; background: var(--rule); }

  .contacts { position: absolute; left: 30px; top: 196px; list-style: none; }
  .contacts li { display: flex; align-items: center; gap: 8px; color: var(--text-light); font-size: 14px; line-height: 25px; }
  .contacts svg { width: 13px; height: 13px; flex: none; }

  .address { position: absolute; right: 30px; top: 200px; text-align: right; color: var(--text-light); font-size: 13px; line-height: 20px; font-style: normal; }
</style>
</head>
<body>
<main class="stage">
  <section class="card card--front" aria-label="Card front">
    <div class="brand">
      <span class="brand__mark"></span>
      <span class="brand__name">Casa Verlaine</span>
    </div>
    <div class="person">
      <p class="person__name">Marcus Ellery</p>
      <p class="person__title">Managing Director</p>
    </div>
    <div class="divider"></div>
    <ul class="contacts">
      <li>
        <svg viewBox="0 0 16 16" fill="var(--gold)"><path d="M3.6 1.2l2.3 2.6-1.3 1.8c.9 2 2.6 3.7 4.6 4.6l1.8-1.3 2.6 2.3-1.3 2.4C6.9 13.4 2.6 9.1 1.2 3.7z"/></svg>
        +31 20 758 4196
      </li>
      <li>
        <svg viewBox="0 0 16 16" fill="var(--gold)"><path d="M1 3h14v10H1z"/><path d="M1 3l7 6 7-6" stroke="var(--card-bg)" stroke-width="1.4" fill="none"/></svg>
        info@casaverlaine.com
      </li>
      <li>
        <svg viewBox="0 0 16 16" fill="none" stroke="var(--gold)" stroke-width="1.4"><circle cx="8" cy="8" r="6.5"/><ellipse cx="8" cy="8" rx="3" ry="6.5"/><path d="M1.5 8h13M2.5 4.8h11M2.5 11.2h11"/></svg>
        www.casaverlaine.com
      </li>
    </ul>
    <address class="address">78, Harbour Crest Avenue<br>7310 KD, Northland</address>
  </section>

  <section class="card card--back" aria-label="Card back">
    <div class="brand">
      <span class="brand__mark"></span>
      <span class="brand__name">Casa Verlaine</span>
    </div>
  </section>
</main>
</body>
</html>
```